Business card for massage therapy company called Brook Fern Wellness

Need business card for massage therapy company called Brook Fern Wellness. Would like my logo on the front and the back of the card I have 3 options of logos and you can play with what looks better.

Would like this information displayed on the back of the card:

Marcus Ellery
Licensed Massage Therapist
321-555-0147
brookfern-example.com
brookfern_rest_

```html
<!DOCTYPE html>
<html lang="en">
<head>
<meta charset="utf-8">
<title>Marcus Ellery – Brook Fern Wellness</title>
<link rel="stylesheet" href="https://fonts.googleapis.com/css2?family=Playfair+Display:wght@700&family=Source+Sans+3:wght@400;700&display=swap">
<style>
  :root {
    --olive: #737b5f;
    --olive-deep: #5f664d;
    --olive-light: #8c9176;
    --skin: #a39a80;
    --cream: #fbf8f1;
    --gold: #f2d6a2;
    --line: #efece2;
  }
  * { margin: 0; padding: 0; box-sizing: border-box; }
  html, body { width: 1200px; height: 686px; overflow: hidden; background: var(--olive); }
  .card {
    position: relative;
    width: 1200px;
    height: 686px;
    overflow: hidden;
    background: var(--olive);
    font-family: "Source Sans 3", "Source Sans Pro", sans-serif;
    color: var(--cream);
  }
  .card__photo {
    position: absolute;
    inset: 0;
    background:
      radial-gradient(ellipse 360px 300px at 330px 300px, rgba(176,164,132,0.55), rgba(176,164,132,0) 70%),
      radial-gradient(ellipse 300px 220px at 130px 220px, rgba(150,158,140,0.45), rgba(150,158,140,0) 70%),
      linear-gradient(90deg, var(--olive-light) 0%, var(--olive) 55%, var(--olive) 100%);
  }
  .brand {
    position: absolute;
    left: 177px;
    top: 171px;
    width: 332px;
    height: 332px;
    border: 3px solid var(--cream);
    border-radius: 50%;
    display: flex;
    align-items: center;
    justify-content: center;
    text-align: center;
  }
  .brand__name {
    font-family: "Playfair Display", serif;
    font-weight: 700;
    font-size: 40px;
    line-height: 1.15;
    color: var(--cream);
  }
  .details {
    position: absolute;
    left: 643px;
    top: 138px;
    width: 450px;
  }
  .details__name {
    font-family: "Playfair Display", serif;
    font-weight: 700;
    font-size: 71px;
    line-height: 1;
    color: var(--cream);
  }
  .details__title {
    margin-top: 18px;
    font-family: "Playfair Display", serif;
    font-weight: 700;
    font-size: 29px;
    color: var(--gold);
  }
  .divider {
    display: block;
    margin-top: 48px;
  }
  .contacts {
    list-style: none;
    margin-top: 42px;
    padding-left: 36px;
  }
  .contact {
    display: flex;
    align-items: center;
    gap: 20px;
    height: 60px;
  }
  .contact__icon { width: 38px; height: 38px; flex: none; display: flex; align-items: center; justify-content: center; color: var(--gold); }
  .contact__icon--at { font-size: 38px; font-weight: 700; line-height: 1; }
  .contact__text { font-size: 35px; font-weight: 400; }
  .contact--phone { height: 72px; }
  .contact--phone .contact__text { font-size: 52px; font-weight: 700; letter-spacing: 1px; }
</style>
</head>
<body>
<div class="card">
  <div class="card__photo" role="img" aria-label="Soft-focus photograph of hands giving a back massage, faded into olive green"></div>

  <div class="brand">
    <span class="brand__name">Brook Fern<br>Wellness</span>
  </div>

  <div class="details">
    <h1 class="details__name">Marcus Ellery</h1>
    <p class="details__title">Licensed Massage Therapist</p>

    <svg class="divider" width="450" height="12" viewBox="0 0 450 12" aria-hidden="true">
      <line x1="0" y1="6" x2="203" y2="6" stroke="var(--line)" stroke-width="2"/>
      <line x1="247" y1="6" x2="450" y2="6" stroke="var(--line)" stroke-width="2"/>
      <path d="M207 6l5-5 5 5-5 5z M220 6l5-5 5 5-5 5z M233 6l5-5 5 5-5 5z" fill="var(--line)"/>
    </svg>

    <ul class="contacts">
      <li class="contact contact--phone">
        <span class="contact__icon">
          <svg width="36" height="36" viewBox="0 0 24 24" aria-hidden="true">
            <path d="M6.6 10.8a15.1 15.1 0 0 0 6.6 6.6l2.2-2.2a1 1 0 0 1 1-.25 11.4 11.4 0 0 0 3.6.57 1 1 0 0 1 1 1V20a1 1 0 0 1-1 1A17 17 0 0 1 3 4a1 1 0 0 1 1-1h3.5a1 1 0 0 1 1 1c0 1.25.2 2.45.57 3.57a1 1 0 0 1-.25 1z" fill="currentColor"/>
            <path d="M14 3.5a6.5 6.5 0 0 1 6.5 6.5M14 7a3 3 0 0 1 3 3" stroke="currentColor" stroke-width="1.8" fill="none" stroke-linecap="round"/>
          </svg>
        </span>
        <span class="contact__text">321-555-0147</span>
      </li>
      <li class="contact">
        <span class="contact__icon">
          <svg width="34" height="34" viewBox="0 0 24 24" aria-hidden="true" fill="none" stroke="currentColor" stroke-width="1.6">
            <circle cx="12" cy="12" r="10"/>
            <ellipse cx="12" cy="12" rx="4.5" ry="10"/>
            <line x1="2" y1="12" x2="22" y2="12"/>
            <line x1="4" y1="7" x2="20" y2="7"/>
            <line x1="4" y1="17" x2="20" y2="17"/>
          </svg>
        </span>
        <span class="contact__text">brookfern-example.com</span>
      </li>
      <li class="contact">
        <span class="contact__icon contact__icon--at">@</span>
        <span class="contact__text">brookfern_rest_</span>
      </li>
    </ul>
  </div>
</div>
</body>
</html>
```